Letter head for peronal trainer

Letter head top and bottom. Elite looking design that looks modern and prestigious for high end clients. Black, silver, reds etc. Attached are my business cards (2 x pdfs) and my website is: www.dariencrofte.example for style/ideas

Needs to look good when printing and be locked onto the page when people use my word docs on the computer, I don't want it to be 'clickable' if you know what I mean. Needs to work in A4 in portrait (and in landscape, for programme cards). I need it to be editable for when I adjust the text myself. Needs my contact details and social media details and title personal trainer (Central London/Greenwich/Blackheath) and Online Distance Coaching. . A little picture at the bottom too if it works (Like the vest one)

```html
<!DOCTYPE html>
<html lang="en">
<head>
<meta charset="utf-8">
<title>Darien Crofte – Personal Trainer Letterhead</title>
<link rel="stylesheet" href="https://fonts.googleapis.com/css2?family=Oswald:wght@700&family=Questrial&display=swap">
<style>
  :root {
    --backdrop: #e6e6e6;
    --paper: #ffffff;
    --ink: #1a1a1a;
    --ink-soft: #555555;
    --name-dark: #4f4f4f;
    --name-light: #a9a9a9;
    --title-grey: #666666;
    --rule: #333333;
    --photo-tone: #d9d9d9;
  }
  * { margin: 0; padding: 0; box-sizing: border-box; }
  html, body {
    width: 1091px;
    height: 1200px;
    overflow: hidden;
    background: var(--backdrop);
  }
  .letterhead {
    position: absolute;
    left: 145px;
    top: 35px;
    width: 800px;
    height: 1130px;
    background: var(--paper);
    font-family: "Questrial", "Century Gothic", sans-serif;
    color: var(--ink);
  }
  .brand-name {
    position: absolute;
    left: 17px;
    top: 18px;
    font-family: "Oswald", "Arial Narrow", sans-serif;
    font-weight: 700;
    font-size: 56px;
    line-height: 56px;
    letter-spacing: 1px;
  }
  .brand-name__first { display: block; color: var(--name-dark); }
  .brand-name__last { display: block; color: var(--name-light); margin-left: 124px; margin-top: -4px; }
  .header-rule {
    position: absolute;
    left: 8px;
    top: 73px;
    width: 771px;
    height: 2px;
    background: var(--rule);
  }
  .job-title {
    position: absolute;
    right: 21px;
    top: 40px;
    font-size: 34px;
    line-height: 34px;
    letter-spacing: 3px;
    color: var(--title-grey);
    white-space: nowrap;
  }
  .service-areas {
    position: absolute;
    right: 21px;
    top: 81px;
    font-size: 12px;
    letter-spacing: 1.6px;
    color: var(--ink);
    white-space: nowrap;
  }
  .hero-photo {
    position: absolute;
    left: 131px;
    top: 209px;
    width: 506px;
    height: 726px;
    background: radial-gradient(ellipse 50% 50% at 50% 50%, var(--photo-tone) 0%, #ececec 55%, rgba(255,255,255,0) 100%);
  }
  .footer-strap {
    position: absolute;
    right: 21px;
    top: 1024px;
    font-size: 26px;
    letter-spacing: 2.6px;
    color: var(--ink);
    white-space: nowrap;
  }
  .footer-rule {
    position: absolute;
    left: 13px;
    top: 1057px;
    width: 766px;
    height: 2px;
    background: var(--rule);
  }
  .contact {
    position: absolute;
    display: flex;
    align-items: center;
    gap: 12px;
    font-size: 16px;
    letter-spacing: 1px;
    color: var(--ink);
    white-space: nowrap;
  }
  .contact svg { width: 16px; height: 16px; fill: var(--ink); flex: none; }
  .contact--phone { left: 18px; top: 1068px; }
  .contact--email { left: 18px; top: 1095px; }
  .contact--web { right: 21px; top: 1068px; }
  .contact--social { right: 21px; top: 1095px; }
  .social-dot { width: 14px; height: 14px; border-radius: 50%; background: var(--ink); flex: none; }
</style>
</head>
<body>
  <main class="letterhead">
    <header>
      <h1 class="brand-name">
        <span class="brand-name__first">DARIEN</span>
        <span class="brand-name__last">CROFTE</span>
      </h1>
      <div class="header-rule"></div>
      <p class="job-title">PERSONAL TRAINER</p>
      <p class="service-areas">CENTRAL LONDON/GREENWICH/BLACKHEATH</p>
    </header>

    <div class="hero-photo" role="img" aria-label="Faded black and white photo of the trainer in a vest lifting dumbbells"></div>

    <footer>
      <p class="footer-strap">ONLINE DISTANCE COACHING</p>
      <div class="footer-rule"></div>

      <p class="contact contact--phone">
        <svg viewBox="0 0 24 24" aria-hidden="true"><path d="M6.6 10.8a15.2 15.2 0 0 0 6.6 6.6l2.2-2.2c.3-.3.7-.4 1-.2 1.1.4 2.3.6 3.6.6.6 0 1 .4 1 1V20c0 .6-.4 1-1 1A17 17 0 0 1 3 4c0-.6.4-1 1-1h3.5c.6 0 1 .4 1 1 0 1.3.2 2.5.6 3.6.1.3 0 .7-.2 1z"/></svg>
        0770090123
      </p>
      <p class="contact contact--email">
        <svg viewBox="0 0 24 24" aria-hidden="true"><path d="M12 2a10 10 0 1 0 0 20 10 10 0 0 0 0-20zm6.9 6h-2.9a15.6 15.6 0 0 0-1.4-3.6A8 8 0 0 1 18.9 8zM12 4c.8 1.2 1.5 2.5 1.9 4h-3.8c.4-1.5 1.1-2.8 1.9-4zM4.3 14a8 8 0 0 1 0-4h3.4a16.5 16.5 0 0 0 0 4zm.8 2h2.9c.3 1.3.8 2.5 1.4 3.6A8 8 0 0 1 5.1 16zM8 8H5.1a8 8 0 0 1 4.3-3.6C8.8 5.5 8.3 6.7 8 8zm4 12c-.8-1.2-1.5-2.5-1.9-4h3.8c-.4 1.5-1.1 2.8-1.9 4zm2.3-6H9.7a14.7 14.7 0 0 1 0-4h4.6a14.7 14.7 0 0 1 0 4zm.3 5.6c.6-1.1 1.1-2.3 1.4-3.6h2.9a8 8 0 0 1-4.3 3.6zm1.7-5.6a16.5 16.5 0 0 0 0-4h3.4a8 8 0 0 1 0 4z"/></svg>
        crofte.dPT@mail.example
      </p>
      <p class="contact contact--web">
        www.dariencrofte.example
        <svg viewBox="0 0 24 24" aria-hidden="true"><path d="M2 5h20v14H2zm2 2v.5l8 5 8-5V7l-8 5z"/></svg>
      </p>
      <p class="contact contact--social">
        @crofty_2
        <span class="social-dot" aria-hidden="true"></span>
      </p>
    </footer>
  </main>
</body>
</html>
```